Die Designerin hat meine Vorstellungen am besten verstanden und umgesetzt. Sie war mir gegenüber sehr verständnisvoll und entgegenkommend. Die Kommunikation mit ihr war sehr erfreulich und sympathisch. Bei meinem nächsten Projekt werde ich mich zuerst an sie wenden.

```html
<!DOCTYPE html>
<html lang="de">
<head>
<meta charset="utf-8">
<title>Mein wunderbarer Sommer in Waldenhof – Buchumschlag</title>
<link rel="stylesheet" href="https://fonts.googleapis.com/css2?family=Cinzel:wght@400;700&display=swap">
<style>
  :root {
    --backdrop-top: #b96b1d;
    --backdrop-bottom: #c9882c;
    --cover: #eba22d;
    --cover-light: #efb047;
    --title-yellow: #f9e413;
    --title-mid: #f8e63a;
    --title-soft: #f8ea6c;
    --title-pale: #f8f0b4;
    --label-red: #c8102e;
    --scooter-red: #e2361f;
    --shadow-orange: #e67a1e;
  }
  * { margin: 0; padding: 0; box-sizing: border-box; }
  html, body {
    width: 1200px;
    height: 1055px;
    overflow: hidden;
  }
  body {
    background: linear-gradient(180deg, var(--backdrop-top), var(--backdrop-bottom));
    position: relative;
    font-family: "Cinzel", serif;
  }
  .book-cover {
    position: absolute;
    left: 282px;
    top: 23px;
    width: 677px;
    height: 1008px;
    background: radial-gradient(ellipse at 50% 45%, var(--cover-light), var(--cover) 70%);
    box-shadow: 0 4px 14px rgba(90, 45, 5, 0.25);
    overflow: hidden;
  }
  .cover-line {
    position: absolute;
    left: 0;
    width: 100%;
    text-align: center;
    line-height: 1;
    white-space: nowrap;
  }
  .genre-label {
    top: 15px;
    font-weight: 700;
    font-size: 29px;
    color: var(--label-red);
  }
  .title { margin: 0; }
  .title .cover-line { font-weight: 400; }
  .line-mein   { top: 98px;  font-size: 43px; color: var(--title-yellow); letter-spacing: 9px;  padding-left: 9px; }
  .line-big    { top: 144px; font-size: 64px; color: var(--title-yellow); letter-spacing: 10px; padding-left: 10px; }
  .line-sommer { top: 215px; font-size: 65px; color: var(--title-mid);    letter-spacing: 12px; padding-left: 12px; }
  .line-in     { top: 290px; font-size: 43px; color: var(--title-soft);   letter-spacing: 8px;  padding-left: 8px; }
  .line-place  { top: 340px; font-size: 65px; color: var(--title-pale);   letter-spacing: 11px; padding-left: 11px; }
  .cover-illustration {
    position: absolute;
    left: 64px;
    top: 420px;
    width: 560px;
    height: 588px;
  }
  .author {
    top: 920px;
    font-weight: 700;
    font-size: 27px;
    letter-spacing: 9px;
    padding-left: 9px;
    color: var(--label-red);
  }
</style>
</head>
<body>
  <main class="book-cover">
    <p class="cover-line genre-label">ROMAN</p>
    <h1 class="title">
      <span class="cover-line line-mein">MEIN</span>
      <span class="cover-line line-big">WUNDERBARER</span>
      <span class="cover-line line-sommer">SOMMER</span>
      <span class="cover-line line-in">IN</span>
      <span class="cover-line line-place">WALDENHOF</span>
    </h1>
    <svg class="cover-illustration" role="img" aria-label="Illustration eines roten Motorrollers mit weißem Sitz, der lange orange Schatten wirft" viewBox="0 0 560 588">
      <defs>
        <radialGradient id="scooter-tone" cx="48%" cy="45%" r="50%">
          <stop offset="0%" stop-color="var(--scooter-red)" stop-opacity="0.85"/>
          <stop offset="55%" stop-color="var(--shadow-orange)" stop-opacity="0.45"/>
          <stop offset="100%" stop-color="var(--cover)" stop-opacity="0"/>
        </radialGradient>
      </defs>
      <rect x="0" y="0" width="560" height="588" fill="url(#scooter-tone)"/>
    </svg>
    <p class="cover-line author">BERNHARD KOLWITZ</p>
  </main>
</body>
</html>
```